Boutique Technology Consultancy specialising is Electronic and physical security

We need to redo our existing outdated website. For your reference the link www.brivo.com.au

```html
<!DOCTYPE html>
<html lang="en">
<head>
<meta charset="utf-8">
<title>Quellan Services — Technology Consulting</title>
<link rel="stylesheet" href="https://fonts.googleapis.com/css2?family=Poppins:wght@500;600;700;800&family=Lexend:wght@300;400;500;600&display=swap">
<style>
:root{
  --red:#8e1b24;
  --red-bright:#c9202c;
  --dark:#2b2b2d;
  --darker:#1e1e20;
  --card:#1f1f21;
  --navy:#1f2547;
  --grey:#6d6f80;
  --light:#f3f3f4;
  --white:#ffffff;
}
*{box-sizing:border-box;margin:0;padding:0}
html,body{width:1200px;height:4504px;overflow:hidden}
body{font-family:"Lexend",sans-serif;color:var(--navy);background:var(--white);position:relative}
a{color:inherit}

/* header + hero */
.hero{position:absolute;left:0;top:0;width:1200px;height:805px;background:linear-gradient(160deg,#4a5567 0%,#2c3646 40%,#1b2433 75%,#242b38 100%)}
.header{position:absolute;left:0;top:0;width:1200px;height:91px;border-bottom:1px solid rgba(255,255,255,.15);display:flex;align-items:center;padding:0 58px}
.brand{display:flex;align-items:center;gap:10px;color:var(--white);font-family:"Poppins",sans-serif;font-weight:700;font-size:30px;letter-spacing:1px}
.brand-mark{width:22px;height:22px;background:var(--red-bright)}
.nav{position:absolute;left:385px;top:35px;display:flex;gap:38px;font-family:"Poppins",sans-serif;font-weight:500;font-size:13px;color:var(--white)}
.nav .active{color:var(--red-bright)}
.header-phone{position:absolute;right:66px;top:24px;height:40px;padding:0 22px;border-radius:20px;background:var(--red-bright);color:var(--white);font-family:"Poppins",sans-serif;font-size:12px;font-weight:600;display:flex;align-items:center;gap:6px}
.hero-title{position:absolute;left:0;top:285px;width:1200px;text-align:center;font-family:"Poppins",sans-serif;font-weight:800;font-size:68px;line-height:80px;color:var(--white);letter-spacing:-1px}
.hero-title span{color:var(--red)}
.btn{display:inline-flex;align-items:center;justify-content:center;background:var(--red-bright);color:var(--white);font-family:"Poppins",sans-serif;font-weight:600;font-size:13px;text-decoration:underline;border-radius:22px}
.hero-btn{position:absolute;left:511px;top:570px;width:187px;height:44px}

/* services */
.services{position:absolute;left:0;top:805px;width:1200px;height:785px;background:var(--dark)}
.service{position:absolute;width:341px;background:var(--card);border-radius:18px;overflow:hidden;box-shadow:0 6px 16px rgba(0,0,0,.35)}
.service::before{content:"";position:absolute;left:50%;top:-70px;width:200px;height:150px;margin-left:-100px;border-radius:50%;background:#262628}
.service svg{position:absolute;left:50%;top:38px;margin-left:-28px}
.service-name{position:absolute;left:20px;right:20px;text-align:center;font-family:"Poppins",sans-serif;font-weight:600;font-size:19px;line-height:22px;color:var(--white);text-decoration:underline}

.cta-band{position:absolute;left:58px;top:1494px;width:1083px;height:160px;border-radius:18px;background:var(--red);color:var(--white)}
.cta-icon{position:absolute;left:46px;top:48px;width:64px;height:64px;border-radius:50%;border:2px solid rgba(255,255,255,.55);display:flex;align-items:center;justify-content:center}
.cta-label{position:absolute;left:131px;top:55px;font-family:"Poppins",sans-serif;font-size:11px;font-weight:600}
.cta-phone{position:absolute;left:131px;top:74px;font-family:"Poppins",sans-serif;font-size:32px;font-weight:700}
.cta-divider{position:absolute;left:494px;top:50px;width:1px;height:62px;background:rgba(255,255,255,.4)}
.cta-text{position:absolute;left:542px;top:57px;width:500px;font-size:13px;line-height:24px}

/* about */
.about-photo{position:absolute;left:107px;top:1770px;width:484px;height:324px;background:linear-gradient(135deg,#1d4f8a 0%,#4c86c0 45%,#f0c060 70%,#2b5d95 100%)}
.years{position:absolute;left:380px;top:1948px;width:145px;height:145px;border-radius:20px;background:var(--white);text-align:center;box-shadow:0 4px 14px rgba(0,0,0,.2)}
.years b{display:block;margin-top:16px;font-family:"Poppins",sans-serif;font-size:50px;line-height:56px;color:var(--red)}
.years span{display:block;font-family:"Poppins",sans-serif;font-size:17px;color:#444}
.years small{display:block;font-size:10px;color:#555;margin-top:6px}
.section-title{font-family:"Poppins",sans-serif;font-weight:700;font-size:42px;color:var(--red)}
.about-title{position:absolute;left:667px;top:1768px}
.about-text{position:absolute;left:667px;top:1845px;width:420px;font-size:14px;line-height:23px;color:var(--grey)}
.about-list{position:absolute;left:667px;top:1943px;list-style:none;font-size:14px;line-height:27px;color:var(--navy)}
.about-list li{display:flex;align-items:center;gap:9px}
.about-btn{position:absolute;left:667px;top:2037px;width:171px;height:44px}

/* experience */
.exp-title{position:absolute;left:0;top:2240px;width:1200px;text-align:center}
.exp-title span{color:var(--navy)}
.exp-text{position:absolute;left:350px;top:2318px;width:500px;text-align:center;font-size:14px;line-height:23px;color:var(--grey)}
.exp-photo{position:absolute;top:2400px;width:250px;height:248px;border-radius:18px}

/* team */
.team{position:absolute;left:0;top:2753px;width:1200px;height:607px;background:var(--dark)}
.member{position:absolute;top:138px;width:243px;height:354px;border-radius:16px;background:var(--white);overflow:hidden}
.member-photo{height:240px}
.member-tag{position:absolute;left:20px;right:20px;top:220px;height:68px;border-radius:16px;background:var(--red);color:var(--white);text-align:center}
.member-tag b{display:block;margin-top:12px;font-family:"Poppins",sans-serif;font-size:19px;text-decoration:underline}
.member-tag small{display:block;font-family:"Poppins",sans-serif;font-size:11px;font-weight:600;line-height:13px}
.socials{position:absolute;left:0;right:0;top:305px;display:flex;justify-content:center;gap:13px}
.socials i{width:26px;height:26px;border-radius:50%;border:1px solid #bbb;display:flex;align-items:center;justify-content:center}
.socials i::after{content:"";width:8px;height:8px;border-radius:50%;background:#333}

/* contact */
.contact{position:absolute;left:0;top:3360px;width:1200px;height:724px;background:linear-gradient(90deg,#f7f7f8 0%,#ececee 60%,#e6e6e8 100%)}
.contact-title{position:absolute;left:107px;top:266px}
.contact-item{position:absolute;left:107px;display:flex;gap:20px}
.contact-icon{width:68px;height:68px;border-radius:50%;background:var(--darker);display:flex;align-items:center;justify-content:center;flex:none}
.contact-item h4{margin-top:12px;font-family:"Poppins",sans-serif;font-weight:500;font-size:17px;color:var(--navy)}
.contact-item p{font-size:13px;color:var(--grey);margin-top:8px}
.form{position:absolute;left:600px;top:115px;width:541px;height:516px;border-radius:24px;background:var(--white);box-shadow:0 6px 24px rgba(0,0,0,.08)}
.form h3{position:absolute;left:0;right:0;top:40px;text-align:center;font-family:"Poppins",sans-serif;font-weight:700;font-size:31px;color:var(--darker)}
.field{position:absolute;left:38px;width:464px;border:1px solid #ddd;border-radius:16px;font-size:12px;color:#999;padding:0 14px}
.submit{position:absolute;left:38px;top:435px;width:178px;height:44px}

/* footer */
.footer{position:absolute;left:0;top:4084px;width:1200px;height:420px;background:var(--dark);color:var(--white)}
.footer .brand{position:absolute;left:58px;top:104px;font-size:38px}
.footer .brand-mark{width:26px;height:26px}
.footer-about{position:absolute;left:58px;top:192px;width:240px;font-size:13px;line-height:24px}
.footer-socials{position:absolute;left:58px;top:288px;display:flex;gap:13px}
.footer-socials i{width:32px;height:32px;border-radius:50%;background:var(--red-bright);display:block}
.footer-col{position:absolute;top:112px}
.footer-col h5{font-family:"Poppins",sans-serif;font-weight:600;font-size:17px}
.footer-col ul{list-style:none;margin-top:22px;font-size:13px;line-height:38.5px}
.footer-contact{font-size:13px;line-height:22px}
.footer-contact p{display:flex;gap:10px}
.copyright{position:absolute;left:0;top:385px;width:1200px;text-align:center;font-size:13px}
</style>
</head>
<body>

<section class="hero" role="img" aria-label="Looking up at glass office towers against the sky, darkened">
  <header class="header">
    <div class="brand"><span class="brand-mark"></span>QUELLAN</div>
    <nav class="nav"><span class="active">HOME</span><span>ABOUT</span><span>SERVICES</span><span>CASE STUDIES</span><span>CONTACT</span></nav>
    <div class="header-phone">
      <svg width="12" height="12" viewBox="0 0 24 24" fill="none" stroke="#fff" stroke-width="2.4"><path d="M5 3h4l2 5-3 2a12 12 0 0 0 6 6l2-3 5 2v4a2 2 0 0 1-2 2A17 17 0 0 1 3 5a2 2 0 0 1 2-2z"/></svg>1300 555 014
    </div>
  </header>
  <h1 class="hero-title">YOUR <span>TECHNOLOGY</span><br>PROJECTS MADE<br>EASY.</h1>
  <a class="btn hero-btn">CONTACT US NOW</a>
</section>

<section class="services">
  <div class="service" style="left:58px;top:113px;height:199px">
    <svg width="56" height="56" viewBox="0 0 56 56" fill="none" stroke="#c9202c" stroke-width="2"><path d="M6 50h46M10 50V36h6v14M22 50V28h6v22M34 50V32h6v18M46 50V20"/><path d="M8 30l14-12 12 8 14-16"/><circle cx="48" cy="9" r="3"/></svg>
    <div class="service-name" style="top:125px">Technology audits</div>
  </div>
  <div class="service" style="left:438px;top:113px;height:199px">
    <svg width="56" height="56" viewBox="0 0 56 56" fill="none" stroke="#c9202c" stroke-width="2"><path d="M6 12l14-5 16 5 14-5v37l-14 5-16-5-14 5z"/><path d="M20 7v37M36 12v37"/><path d="M12 30l8-6 8 8 10-10 8 6"/></svg>
    <div class="service-name" style="top:125px">Technology roadmaps</div>
  </div>
  <div class="service" style="left:800px;top:113px;height:199px">
    <svg width="56" height="56" viewBox="0 0 56 56" fill="none" stroke="#c9202c" stroke-width="2"><path d="M4 28l10-8 8 4 8-6 10 4 12 6"/><path d="M14 20l-8 14 14 12 12-2 14-14"/><path d="M28 4v6M18 8l3 5M38 8l-3 5"/></svg>
    <div class="service-name" style="top:125px">Technology designs</div>
  </div>
  <div class="service" style="left:58px;top:352px;height:222px">
    <svg width="56" height="56" viewBox="0 0 56 56" fill="none" stroke="#c9202c" stroke-width="2"><path d="M8 4h26l8 8v18M8 4v46h22"/><path d="M14 16h14M14 24h12M14 32h8"/><circle cx="38" cy="38" r="8"/><path d="M44 44l8 8"/></svg>
    <div class="service-name" style="top:133px">Technology procurement</div>
  </div>
  <div class="service" style="left:438px;top:352px;height:222px">
    <svg width="56" height="56" viewBox="0 0 56 56" fill="none" stroke="#c9202c" stroke-width="2"><path d="M10 4h30v48H10z"/><circle cx="25" cy="18" r="6"/><path d="M16 32h18M16 40h14"/><path d="M44 20l6 6-14 20-6 2 2-6z"/></svg>
    <div class="service-name" style="top:133px">Technology project<br>management</div>
  </div>
  <div class="service" style="left:800px;top:352px;height:222px">
    <svg width="56" height="56" viewBox="0 0 56 56" fill="none" stroke="#c9202c" stroke-width="2"><rect x="16" y="16" width="24" height="24" rx="4"/><path d="M28 4v8M28 44v8M4 28h8M44 28h8"/><circle cx="28" cy="6" r="3"/><circle cx="28" cy="50" r="3"/><circle cx="6" cy="28" r="3"/><circle cx="50" cy="28" r="3"/></svg>
    <div class="service-name" style="top:133px">Digital Market Planning</div>
  </div>
</section>

<div class="cta-band">
  <div class="cta-icon"><svg width="30" height="30" viewBox="0 0 24 24" fill="none" stroke="#fff" stroke-width="1.4"><path d="M5 3h4l2 5-3 2a12 12 0 0 0 6 6l2-3 5 2v4a2 2 0 0 1-2 2A17 17 0 0 1 3 5a2 2 0 0 1 2-2z"/><path d="M14 3a7 7 0 0 1 7 7M14 7a3 3 0 0 1 3 3"/></svg></div>
  <div class="cta-label">GET A FREE CONSULTATION</div>
  <div class="cta-phone">1300 555 014</div>
  <div class="cta-divider"></div>
  <p class="cta-text">Quellan Services provides independent professional services for projects as well as operations and maintenance.</p>
</div>

<div class="about-photo" role="img" aria-label="Glass office tower with sunlight flaring across its facade"></div>
<div class="years"><b>08</b><span>YEARS</span><small>OF EXPERIENCE</small></div>
<h2 class="section-title about-title">About Us</h2>
<p class="about-text">Quellan Services was established in 2016 by Glen Harrow to provide technology consulting services to corporate and government clients with a focus on</p>
<ul class="about-list">
  <li><svg width="15" height="15" viewBox="0 0 16 16" fill="none" stroke="#c9202c" stroke-width="1.5"><circle cx="8" cy="8" r="6.5"/><path d="M5 8l2 2 4-4"/></svg>Property/facilities management</li>
  <li><svg width="15" height="15" viewBox="0 0 16 16" fill="none" stroke="#c9202c" stroke-width="1.5"><circle cx="8" cy="8" r="6.5"/><path d="M5 8l2 2 4-4"/></svg>Asset management</li>
  <li><svg width="15" height="15" viewBox="0 0 16 16" fill="none" stroke="#c9202c" stroke-width="1.5"><circle cx="8" cy="8" r="6.5"/><path d="M5 8l2 2 4-4"/></svg>Development and Construction</li>
</ul>
<a class="btn about-btn">MORE ABOUT US</a>

<h2 class="section-title exp-title">Our <span>Experience</span></h2>
<p class="exp-text">Quellan has a diverse range of project experience across a range of industries within both the public and private sectors.</p>
<div class="exp-photo" style="left:58px;background:linear-gradient(180deg,#d8d8d8 0%,#7a7a7a 55%,#2a2a2a 100%)" role="img" aria-label="Black and white road with overhead signage and cars"></div>
<div class="exp-photo" style="left:336px;background:linear-gradient(180deg,#3a3a3a 0%,#bdbdbd 50%,#3a3a3a 100%)" role="img" aria-label="Black and white glass atrium interior"></div>
<div class="exp-photo" style="left:614px;background:linear-gradient(180deg,#f2f2f2 0%,#6b6b6b 45%,#222 100%)" role="img" aria-label="Black and white high-rise towers"></div>
<div class="exp-photo" style="left:892px;background:linear-gradient(180deg,#cfcfcf 0%,#5e5e5e 55%,#1c1c1c 100%)" role="img" aria-label="Black and white building entrance with stairs"></div>

<section class="team">
  <div class="member" style="left:72px">
    <div class="member-photo" role="img" aria-label="Portrait of Glen Harrow" style="background:linear-gradient(180deg,#8a7868,#c9a58a)"></div>
    <div class="member-tag"><b>Glen Harrow</b><small>Principal Consultant</small></div>
    <div class="socials"><i></i><i></i><i></i><i></i></div>
  </div>
  <div class="member" style="left:343px">
    <div class="member-photo" role="img" aria-label="Portrait of Neil Packard" style="background:linear-gradient(180deg,#7b7f86,#c2a592)"></div>
    <div class="member-tag"><b>Neil Packard</b><small>Principal Consultant</small></div>
    <div class="socials"><i></i><i></i><i></i><i></i></div>
  </div>
  <div class="member" style="left:614px">
    <div class="member-photo" role="img" aria-label="Portrait of Marco Devlin" style="background:linear-gradient(180deg,#3a3d42,#a8887a)"></div>
    <div class="member-tag"><b>Marco Devlin</b><small>Senior Consultant</small></div>
    <div class="socials"><i></i><i></i><i></i><i></i></div>
  </div>
  <div class="member" style="left:885px">
    <div class="member-photo" role="img" aria-label="Portrait of Lina Chow" style="background:linear-gradient(180deg,#ececec,#d9c4b8)"></div>
    <div class="member-tag" style="height:78px"><b style="margin-top:10px">Lina Chow</b><small>Administration<br>Coordinator</small></div>
    <div class="socials" style="top:318px"><i></i><i></i><i></i><i></i></div>
  </div>
</section>

<section class="contact">
  <h2 class="section-title contact-title">Contact Us</h2>
  <div class="contact-item" style="top:337px">
    <div class="contact-icon"><svg width="28" height="28" viewBox="0 0 24 24" fill="none" stroke="#fff" stroke-width="1.4"><path d="M12 22s7-7 7-12a7 7 0 0 0-14 0c0 5 7 12 7 12z"/><circle cx="12" cy="10" r="2.5"/></svg></div>
    <div><h4>Office Address :</h4><p>PO Box 7712 HOBART TAS 7001</p></div>
  </div>
  <div class="contact-item" style="top:435px">
    <div class="contact-icon"><svg width="28" height="28" viewBox="0 0 24 24" fill="none" stroke="#fff" stroke-width="1.4"><path d="M5 3h4l2 5-3 2a12 12 0 0 0 6 6l2-3 5 2v4a2 2 0 0 1-2 2A17 17 0 0 1 3 5a2 2 0 0 1 2-2z"/></svg></div>
    <div><h4>Phone Number :</h4><p>1300 555 014</p></div>
  </div>
  <div class="contact-item" style="top:533px">
    <div class="contact-icon"><svg width="28" height="28" viewBox="0 0 24 24" fill="none" stroke="#fff" stroke-width="1.4"><path d="M3 10l9-6 9 6v10H3z"/><path d="M3 10l9 6 9-6"/></svg></div>
    <div><h4>Mail Address :</h4><p>hello@quellanservices.com.au</p></div>
  </div>
  <form class="form">
    <h3>Get In Touch !</h3>
    <div class="field" style="top:95px;height:52px;line-height:52px">Your Name*</div>
    <div class="field" style="top:168px;height:52px;line-height:52px">Your Email*</div>
    <div class="field" style="top:241px;height:174px;padding-top:18px">Enter Message</div>
    <a class="btn submit">SUBMIT MESSAGE</a>
  </form>
</section>

<footer class="footer">
  <div class="brand"><span class="brand-mark"></span>QUELLAN</div>
  <p class="footer-about">We provide technology consulting services to corporate and government clients.</p>
  <div class="footer-socials"><i></i><i></i><i></i><i></i></div>
  <div class="footer-col" style="left:343px"><h5>Useful Links</h5><ul><li>About us</li><li>Services</li><li>Experience</li><li>Team</li></ul></div>
  <div class="footer-col" style="left:614px"><h5>Support</h5><ul><li>Help Center</li><li>Contact Us</li><li>FAQ</li><li>Parent Community</li></ul></div>
  <div class="footer-col" style="left:885px;width:260px">
    <h5>Contact Information</h5>
    <div class="footer-contact">
      <p style="margin-top:22px">Feel free to contact &amp; reach us !!</p>
      <p style="margin-top:18px;padding-left:28px">PO Box 7712 HOBART TAS 7001</p>
      <p style="margin-top:12px;padding-left:28px">1300 555 014</p>
      <p style="margin-top:12px;padding-left:28px">hello@quellanservices.com.au</p>
    </div>
  </div>
  <p class="copyright">Copyright © 2023 Quellan. All rights reserved.</p>
</footer>

</body>
</html>
```